Web Page Header (Header Only)

Our company would like to develop a new website header look for our business webpage theme. This header needs to look fantastic and add value to the overall professional appearance of our business and website design. We would like to incorporate into the design concept our company logo and use the slogan “Providing Effect Project Controls and Management Solutions” It would be great to promote our businesses global presence in the website header design concept.

For you to understand our business branding, images of our business cards, company brochure and Facebook page have been attached to this project. A PDF file of our company logo is also attached, our website address is www.brightlanepartners.com Please read the attached webpage header PDF document attached to this project as it will you assist with your design concept. Contained within the PDF is also an example of a webpage header design.

The graphic design work needs to done in Photoshop as our business utilizes CS6. The winning design concept will be integrated into our webpage theme using our original website developer. The graphics will need to fit the dimensions for our webpage header area for easy integration.
Updates

It would be great to promote our busineses global presence in the website header design concept

Project Deadline Extended
Reason: Some designers needed more time

Industry/Entity Type

Graphic Design

Requirements
Must have
• The webpage header design must be elegant, professional,reflect a market leader and be easily integrate into the webpage design.

```html
<!DOCTYPE html>
<html lang="en">
<head>
<meta charset="utf-8">
<title>Brightlane Partners – Header</title>
<link rel="stylesheet" href="https://fonts.googleapis.com/css2?family=Russo+One&family=Arimo:wght@400&display=swap">
<style>
  :root {
    --ink: #000000;
    --paper: #ffffff;
    --signal-red: #ee1111;
  }
  * { margin: 0; padding: 0; box-sizing: border-box; }
  html, body {
    width: 1200px;
    height: 384px;
    overflow: hidden;
    background: var(--paper);
  }
  .header {
    position: relative;
    width: 1200px;
    height: 384px;
    background: var(--paper);
    overflow: hidden;
  }
  .header__sweep {
    position: absolute;
    inset: 0;
    width: 1200px;
    height: 384px;
  }
  .brand-mark {
    position: absolute;
    left: 40px;
    top: 174px;
    display: flex;
    align-items: center;
    gap: 10px;
  }
  .brand-mark__square {
    width: 30px;
    height: 30px;
    background: var(--signal-red);
  }
  .brand-mark__name {
    font-family: "Russo One", sans-serif;
    font-size: 27px;
    line-height: 1;
    color: var(--ink);
  }
  .brand-panel {
    position: absolute;
    left: 328px;
    top: 104px;
    width: 500px;
    height: 168px;
    background: var(--paper);
    display: flex;
    flex-direction: column;
    align-items: center;
    justify-content: center;
    gap: 18px;
    padding-top: 6px;
  }
  .brand-panel__name {
    font-family: "Russo One", sans-serif;
    font-size: 62px;
    line-height: 1;
    color: var(--ink);
    letter-spacing: 1px;
  }
  .brand-panel__tagline {
    font-family: "Arimo", sans-serif;
    font-size: 25px;
    line-height: 1;
    color: var(--ink);
  }
  .service-line {
    position: absolute;
    left: 860px;
    top: 133px;
  }
  .service-line__title {
    font-family: "Russo One", sans-serif;
    font-size: 48px;
    line-height: 44px;
    color: var(--signal-red);
    letter-spacing: 1px;
  }
  .service-line__sub {
    margin-top: 12px;
    font-family: "Arimo", sans-serif;
    font-size: 23px;
    line-height: 1;
    color: var(--paper);
  }
</style>
</head>
<body>
  <header class="header">
    <svg class="header__sweep" viewBox="0 0 1200 384" aria-hidden="true">
      <path d="M364 0 Q212 192 364 384 L1200 384 L1200 0 Z" fill="var(--ink)"/>
    </svg>

    <div class="brand-mark">
      <span class="brand-mark__square"></span>
      <span class="brand-mark__name">BRIGHTLANE</span>
    </div>

    <div class="brand-panel">
      <div class="brand-panel__name">BRIGHTLANE</div>
      <div class="brand-panel__tagline">Providing Effective Project Controls</div>
    </div>

    <div class="service-line">
      <div class="service-line__title">PROJECT<br>SOLUTIONS</div>
      <div class="service-line__sub">and Management Solutions</div>
    </div>
  </header>
</body>
</html>
```